Holistic/ Sports Psychologist needs flyer design

I need a flyer designed that catches the attention of potential customers - (parents of young athletes and athletes) who may be looking for psychological services. I have a logo and all the relevant info for the flyer but would like someone to take it and make it look creative, fun, fresh and attention getting for high school and college athletes. The colors used can be from my logo design which represents my holistic approach.
Target Market(s)
high school and collegiate athletes
Industry/Entity Type
sports psychology
Requirements
Must have
- Info I put on the flyer with my logo and please add some graphics and color based on my logo

```html
<!DOCTYPE html>
<html lang="en">
<head>
<meta charset="utf-8">
<title>Holistic & Sports Psychology Consulting Flyer</title>
<link href="https://fonts.googleapis.com/css2?family=Chewy&family=Itim&family=Poppins:wght@400;500;600&family=Yellowtail&display=swap" rel="stylesheet">
<style>
:root{
  --green:#a9d27a;
  --green-dark:#4d6b2e;
  --blue:#46739d;
  --purple:#5a3f9a;
  --yellow:#f4b512;
  --paper:#f7f5f2;
  --ink:#2b2b2b;
  --white:#ffffff;
}
*{margin:0;padding:0;box-sizing:border-box}
html,body{width:862px;height:1200px;overflow:hidden;background:#fff}
.flyer{position:relative;width:862px;height:1200px;background:var(--white);overflow:hidden;font-family:'Poppins',sans-serif;color:var(--ink)}
.backdrop{position:absolute;left:0;top:0;width:862px;height:950px;background:linear-gradient(90deg,var(--green) 0%,#8fbd7d 40%,#5f8b96 70%,var(--blue) 100%)}
.abs{position:absolute}
.athletes-photo{left:93px;top:25px;width:316px;height:412px;border-radius:40px 40px 10px 10px;background:linear-gradient(180deg,rgba(60,90,160,.35),rgba(30,40,70,.5))}
.paper{left:40px;top:300px;width:470px;height:760px}
.cloud{left:320px;top:40px;width:525px;height:240px}
.amp{left:398px;top:136px;width:40px;height:40px;border-radius:50%;background:var(--purple);color:#fff;font-family:'Chewy',cursive;font-size:24px;display:flex;align-items:center;justify-content:center;border:2px solid #fff}
.title{font-family:'Chewy',cursive;line-height:1;white-space:nowrap}
.title-holistic{left:444px;top:96px;font-size:44px;color:var(--green-dark)}
.title-sports{left:440px;top:136px;font-size:46px;color:var(--yellow)}
.title-consult{left:535px;top:186px;font-family:'Yellowtail',cursive;font-size:36px;color:var(--purple)}
.portrait{left:514px;top:306px;width:120px;height:120px;border-radius:50%;border:2px solid var(--yellow);background:radial-gradient(circle at 50% 40%,#dfe3e8,#9aa5b4);}
.dr-name{left:644px;top:334px;font-family:'Itim',cursive;font-size:22px;line-height:23px;color:#fff}
.badge{left:633px;top:391px;width:166px;height:30px;border-radius:0 15px 15px 0;background:var(--purple);color:#fff;font-size:10.5px;font-weight:600;display:flex;align-items:center;justify-content:center}
.badge span{color:var(--yellow);margin-left:3px}
.bg-head{left:516px;top:443px;font-family:'Itim',cursive;font-size:26px;color:#fff}
.bio{left:516px;width:300px;font-size:12.6px;line-height:15.3px;color:#fff}
.bio-1{top:486px}
.bio-2{top:645px}
.rule-right{left:516px;top:747px;width:290px;height:1px;background:rgba(255,255,255,.6)}
.online{left:519px;top:759px;font-family:'Itim',cursive;font-size:19px;line-height:23px;color:#fff}
.pill{left:521px;top:812px;width:232px;height:32px;border-radius:16px;background:var(--yellow);color:var(--purple);font-family:'Itim',cursive;font-size:16px;display:flex;align-items:center;justify-content:center;box-shadow:0 2px 3px rgba(0,0,0,.2)}
.circle-photo{width:140px;height:140px;border-radius:50%;border:2px solid var(--yellow)}
.photo-session{left:514px;top:878px;background:linear-gradient(160deg,#8d8f7a,#4f5748)}
.photo-beach{left:668px;top:878px;background:linear-gradient(180deg,#bcd8ee 0%,#e8eef2 60%,#d8cfb8 100%)}
.contact-head{left:519px;top:1042px;font-family:'Itim',cursive;font-size:20px;color:var(--green-dark)}
.contact{left:519px;width:300px;font-size:11.5px;font-weight:500;line-height:14px;display:flex;gap:8px;align-items:flex-start}
.contact svg{flex:none;margin-top:0}
.c-phone{top:1082px}.c-pin{top:1102px}.c-web{top:1136px}
.list-head{left:93px;top:465px;font-family:'Chewy',cursive;font-size:20px;line-height:23px;color:var(--purple)}
.list-head span{color:var(--green-dark)}
.item{left:93px;width:365px}
.item .icon{position:absolute;left:0;top:0;width:29px;height:29px;border-radius:5px;display:flex;align-items:center;justify-content:center}
.item h3{position:absolute;left:38px;top:-2px;font-family:'Itim',cursive;font-weight:400;font-size:16px;color:var(--purple);white-space:nowrap}
.item p{position:absolute;left:38px;top:20px;width:300px;font-size:11px;line-height:14px}
.i1{top:547px}.i2{top:623px}.i3{top:712px}.i4{top:803px}.i5{top:919px}
.i2 h3,.i4 h3{color:var(--green-dark)}
.ic-blue{background:#a7cbe8}.ic-green{background:#a5cf75}.ic-yellow{background:var(--yellow)}
.rule-left{left:93px;width:362px;height:1px;background:#b8b8b8}
.logo-dot{left:55px;top:1053px;width:100px;height:100px;border-radius:50%;background:var(--blue)}
.logo-name{left:170px;top:1079px;font-family:'Poppins',sans-serif;font-size:25px;font-weight:400;color:var(--blue);white-space:nowrap}
.logo-bar{left:155px;top:1111px;width:316px;height:20px;background:var(--green)}
</style>
</head>
<body>
<main class="flyer">
  <div class="backdrop"></div>

  <svg class="abs paper" viewBox="0 0 470 760" aria-hidden="true">
    <path fill="#f7f5f2" d="M20 40 L60 12 L120 22 L180 8 L250 18 L310 6 L370 20 L410 30 L418 70 L440 110 L432 170 L446 230 L436 300 L450 380 L440 460 L452 540 L444 620 L456 690 L420 730 L360 744 L290 736 L220 752 L150 740 L90 748 L40 732 L20 690 L8 620 L16 540 L4 460 L14 380 L2 300 L12 220 L0 140 L12 90 Z"/>
  </svg>
  <div class="abs athletes-photo" role="img" aria-label="Photo of three young athletes in sportswear, one holding a basketball"></div>

  <svg class="abs cloud" viewBox="0 0 525 240" aria-hidden="true">
    <g fill="#4d6b2e">
      <circle cx="120" cy="130" r="80"/><circle cx="230" cy="90" r="78"/><circle cx="340" cy="100" r="80"/><circle cx="430" cy="135" r="82"/><circle cx="300" cy="170" r="68"/><circle cx="170" cy="175" r="60"/><circle cx="400" cy="180" r="55"/>
    </g>
    <g fill="#fdfafd">
      <circle cx="118" cy="124" r="78"/><circle cx="228" cy="84" r="76"/><circle cx="338" cy="94" r="78"/><circle cx="428" cy="128" r="80"/><circle cx="298" cy="162" r="66"/><circle cx="168" cy="168" r="58"/><circle cx="398" cy="172" r="53"/>
    </g>
  </svg>
  <div class="abs amp">&amp;</div>
  <div class="abs title title-holistic">Holistic Psychology</div>
  <div class="abs title title-sports">Sports Psychology</div>
  <div class="abs title title-consult">Consulting</div>

  <div class="abs portrait" role="img" aria-label="Portrait photo of the psychologist"></div>
  <div class="abs dr-name">Dr. Rosalind<br>Carrow</div>
  <div class="abs badge">LICENSED<span>PSYCHOLOGIST</span></div>

  <h2 class="abs bg-head" style="font-weight:400">Background</h2>
  <p class="abs bio bio-1">Dr. Rosalind Carrow is a licensed psychologist. She understands the unique experiences of athletes due to her background as an All American swimmer, collegiate and age group swim coach, parent of a collegiate/professional athlete, and sports psychology researcher. She works with athletes to optimize performance and overall well-being.</p>
  <p class="abs bio bio-2">Her specializations include: performance anxiety, mental performance, stress management, anxiety, depressions, trauma, life transitions, relationship issues, injury, and sleep.</p>
  <div class="abs rule-right"></div>
  <p class="abs online">All services are provided online<br>via telehealth.</p>
  <div class="abs pill">Sessions are 30 or 55 minutes</div>

  <div class="abs circle-photo photo-session" role="img" aria-label="Photo of a counselling session with a young woman"></div>
  <div class="abs circle-photo photo-beach" role="img" aria-label="Photo of a family walking on a beach with a dog"></div>

  <h2 class="abs contact-head" style="font-weight:400">Contact us for more information</h2>
  <div class="abs contact c-phone">
    <svg width="14" height="14" viewBox="0 0 14 14"><circle cx="7" cy="7" r="7" fill="#46739d"/><path d="M4.5 3.5l1.5 0 .6 1.8-.9.7a5 5 0 0 0 2.3 2.3l.7-.9 1.8.6v1.5c-3.5.4-6.4-2.5-6-6z" fill="#fff"/></svg>
    <span>555-014-2290</span>
  </div>
  <div class="abs contact c-pin">
    <svg width="14" height="14" viewBox="0 0 14 14"><circle cx="7" cy="7" r="7" fill="#46739d"/><path d="M7 3a2.5 2.5 0 0 1 2.5 2.5C9.5 7.5 7 10.5 7 10.5S4.5 7.5 4.5 5.5A2.5 2.5 0 0 1 7 3z" fill="#fff"/><circle cx="7" cy="5.5" r=".9" fill="#46739d"/></svg>
    <span>820 Harbor Lane #114 Seabrook Point,<br>FL 30000</span>
  </div>
  <div class="abs contact c-web">
    <svg width="14" height="14" viewBox="0 0 14 14"><circle cx="7" cy="7" r="7" fill="#46739d"/><circle cx="7" cy="7" r="3.6" fill="none" stroke="#fff" stroke-width="1"/><path d="M3.4 7h7.2M7 3.4c-1.5 2-1.5 5.2 0 7.2M7 3.4c1.5 2 1.5 5.2 0 7.2" stroke="#fff" stroke-width=".8" fill="none"/></svg>
    <span>www.drrosalindcarrow.com</span>
  </div>

  <h2 class="abs list-head" style="font-weight:400">Ways to Improve Athletic Performance<br><span>Using Sports and Holistic Psychology</span></h2>

  <section class="abs item i1">
    <div class="icon ic-blue"><svg width="17" height="17" viewBox="0 0 17 17"><circle cx="8.5" cy="8" r="6" fill="#5a3f9a"/></svg></div>
    <h3>Mental Skills Training</h3>
    <p>Ex: visualization, goal-setting, motivation, self- talk, mindset, concentration techniques</p>
  </section>
  <div class="abs rule-left" style="top:602px"></div>
  <section class="abs item i2">
    <div class="icon ic-green"><svg width="17" height="17" viewBox="0 0 17 17"><path d="M8.5 2l3 4h-2v8h-2V6h-2z" fill="#5a3f9a"/></svg></div>
    <h3>Performance Enhancement</h3>
    <p>Eliminate psychological barriers that are hindering performance such as self- doubt, perfectionism, fear of failure, and burnout</p>
  </section>
  <div class="abs rule-left" style="top:691px"></div>
  <section class="abs item i3">
    <div class="icon ic-yellow"><svg width="17" height="17" viewBox="0 0 17 17"><path d="M8.5 14.5S2 10.5 2 6.3A3.2 3.2 0 0 1 8.5 5a3.2 3.2 0 0 1 6.5 1.3c0 4.2-6.5 8.2-6.5 8.2z" fill="#5a3f9a"/></svg></div>
    <h3>Mental Health</h3>
    <p>anxiety and stress management by using relaxation techniques, breathwork, and mindfulness practices</p>
  </section>
  <div class="abs rule-left" style="top:781px"></div>
  <section class="abs item i4">
    <div class="icon ic-blue"><svg width="17" height="17" viewBox="0 0 17 17"><path d="M7 2h3v5h5v3h-5v5H7v-5H2V7h5z" fill="#5a3f9a"/></svg></div>
    <h3>Injury Recovery Support</h3>
    <p>Assist athletes in maintaining resilience and positive mental attitude during rehabilitation as well as processing emotions relating to any potential trauma caused by the injury or life transitions resulting from it</p>
  </section>
  <div class="abs rule-left" style="top:899px"></div>
  <section class="abs item i5">
    <div class="icon ic-green"><svg width="17" height="17" viewBox="0 0 17 17"><circle cx="8.5" cy="8.5" r="6" fill="none" stroke="#5a3f9a" stroke-width="2"/><path d="M5.5 8.5l2 2 4-4" stroke="#5a3f9a" stroke-width="2" fill="none"/></svg></div>
    <h3>Burnout prevention</h3>
    <p>Teach athletes how to have balance in sports and life so they can experience longevity in their sports as well as overall optimal health and well-being</p>
  </section>

  <div class="abs logo-dot"></div>
  <div class="abs logo-bar"></div>
  <div class="abs logo-name">Dr. Rosalind Carrow</div>
</main>
</body>
</html>
```